Door Hanger Design for Electricians Serving Homes

I would like our logo incorporated into the door hanger. We would like a place for a tear off section on the bottom of the hanger with our contact information: K&T Electric - (555) 318-4702 - www.kandtelectric.example - info@kandtelectric.example.
Door Hanger Script
Front Side of the Door Hanger:
[Company Logo]
Need a Reliable Electrician?
Your Local Electrical Expert is Just Around the Corner!
• Quick Response Times
• Affordable Rates
• Quality Workmanship
• Fully Licensed & Insured
• Special Offer:
• 10% OFF Your First Service Call!
Back Side of the Door Hanger:
Don't Let Electrical Issues Keep You in the Dark!
From flickering lights to complete system upgrades, we've got all your
residential electrical needs covered. Our services include:
• Electrical Repairs & Troubleshooting
• Lighting Installation & Upgrades
• Safety Inspections & Code Compliance
• Energy-Efficient Solutions
• 24/7 Emergency Services
• Why Choose Us?
• Friendly, Local Service
• Over 30 Years of Experience
• Satisfaction Guaranteed
• Upfront Pricing
Call Us Today: [Your Phone Number]
Visit Our Website: [Your Website]
Book Your Appointment Now and Claim Your 10% Discount!
Offer valid for new customers on the first visit only. Mention this door hanger when
booking.
[Your Company Name and Contact Information]
Follow Us on Social Media for More Tips and Special Offers!
[Icons for social media platforms: Chatterpage, Pixmosaic, Quibbler, etc.]
Design Tips:
Use bold, clear fonts for easy reading.
Incorporate your brand colors and logo for instant recognition.
Include a clear call to action (CTA) on both sides.
Add a tear-off section at the bottom with your contact information for
convenience.
Use high-quality images or graphics related to electrical work to catch
the eye.
This door hanger design and copy aim to attract residential clients by
highlighting the benefits of your electrical services, special offers, and
how they can easily get in touch with you for their electrical needs.
The door knocker template will have three of the same design on front and three of the same design on the back. This template is from the print shop.

```html
<!DOCTYPE html>
<html lang="en">
<head>
<meta charset="utf-8">
<title>K&amp;T Electric Door Hanger</title>
<link href="https://fonts.googleapis.com/css2?family=Poppins:wght@400;500;600;700;800&family=Oswald:wght@500;600;700&display=swap" rel="stylesheet">
<style>
:root{
  --page:#ececec;
  --navy:#15213b;
  --navy-deep:#0c1425;
  --red:#e8141b;
  --yellow:#ffd400;
  --ink:#1b1b1b;
  --white:#ffffff;
  --grey:#8a8a8a;
}
*{box-sizing:border-box;margin:0;padding:0}
html,body{width:1200px;height:2400px;overflow:hidden;background:var(--page);font-family:"Poppins",sans-serif;color:var(--ink)}
.hanger{position:absolute;top:600px;width:520px;height:1200px;background:var(--white);overflow:hidden;box-shadow:0 6px 18px rgba(0,0,0,.25)}
.hanger--front{left:50px}
.hanger--back{left:630px}
.layer{position:absolute;left:0;top:0;width:520px;height:1200px}
.abs{position:absolute}
.hole{position:absolute;left:188px;top:85px;width:144px;height:144px;border-radius:50%;background:var(--page);box-shadow:inset 0 6px 10px rgba(0,0,0,.35)}
.hanger--back .hole{left:186px;top:88px}

/* front */
.front-photo{position:absolute;left:0;top:0;width:520px;height:950px;background:
 radial-gradient(ellipse at 55% 70%,#6b4a2a 0%,rgba(60,45,35,.6) 28%,rgba(0,0,0,0) 55%),
 linear-gradient(180deg,#1b2a48 0%,#243456 35%,#2a2e38 60%,#1a1d24 100%)}
.brand{left:0;width:520px;top:258px;text-align:center;color:var(--white)}
.brand-name{font-weight:700;font-size:54px;line-height:1;letter-spacing:1px}
.brand-sub{font-weight:700;font-size:22px;letter-spacing:1px;margin-top:8px}
.front-head{left:0;width:520px;top:395px;text-align:center}
.front-head h1{font-weight:700;font-size:36px;line-height:36px;color:var(--white)}
.front-head h1 span{color:var(--red);display:block}
.front-head p{color:var(--white);font-size:15px;margin-top:8px}
.offer-badge{left:340px;top:650px;width:140px;height:140px}
.offer-text{left:340px;top:676px;width:140px;text-align:center;color:var(--white)}
.offer-text small{display:block;font-size:13px;line-height:16px;font-weight:500}
.offer-text b{display:block;font-weight:800;font-size:36px;line-height:35px;color:var(--yellow)}
.offer-line{right:36px;top:808px;text-align:center;font-weight:700;font-size:20px;line-height:22px;color:var(--ink)}
.feature{top:888px;width:124px;text-align:center}
.feature svg{width:74px;height:74px;display:block;margin:0 auto}
.feature span{display:block;font-weight:500;font-size:15px;line-height:18px;margin-top:4px}

/* contact strip (tear-off) */
.tear{left:0;top:1040px;width:520px;border-top:1.5px dashed #bdbdbd}
.call{left:24px;top:1058px;width:466px;height:44px;border-radius:22px;background:var(--red)}
.call-label{position:absolute;left:0;top:0;height:44px;width:176px;border-radius:22px 0 0 22px;background:var(--ink);color:var(--white);font-family:"Oswald",sans-serif;font-weight:500;font-size:22px;line-height:44px;padding-left:16px}
.call-icon{position:absolute;left:160px;top:8px;width:28px;height:28px;border-radius:50%;background:var(--white);border:2px solid var(--ink)}
.call-icon svg{width:24px;height:24px}
.call-num{position:absolute;left:194px;top:0;line-height:44px;font-family:"Oswald",sans-serif;font-weight:600;font-size:34px;color:var(--white)}
.link-box{top:1118px;height:36px;border:1.5px dashed var(--red);border-radius:6px;text-align:center;font-weight:600;font-size:13px;line-height:33px}
.link-box--mail{left:24px;width:234px}
.link-box--web{left:262px;width:234px}
.link-dot{position:absolute;left:50%;top:-12px;margin-left:-11px;width:22px;height:22px;border-radius:50%;background:var(--red);border:2px solid var(--white)}
.social{left:0;top:1168px;width:520px;text-align:center;font-size:9px;line-height:14px;white-space:nowrap}
.social b{font-weight:600;color:var(--navy)}
.social i{display:inline-block;width:8px;height:8px;border-radius:50%;background:var(--navy);margin:0 2px 0 4px;vertical-align:0}

/* back */
.back-photo{left:0;top:0;width:520px;height:260px}
.emergency{left:345px;top:55px;width:150px;height:150px}
.emergency-text{left:350px;top:100px;width:140px;text-align:center;font-family:"Oswald",sans-serif;transform:rotate(-10deg)}
.emergency-text b{display:block;font-size:42px;line-height:40px;color:var(--red);font-weight:700}
.emergency-text b small{font-size:20px}
.emergency-text span{display:block;font-size:19px;line-height:18px;font-weight:700;color:var(--ink)}
.emergency-text em{display:block;font-style:normal;font-size:12px;line-height:13px;font-weight:700;color:var(--red);letter-spacing:1px}
.back-head{left:0;width:520px;top:255px;text-align:center}
.back-head h2{font-weight:700;font-size:30px;line-height:38px;color:var(--ink)}
.back-head h2 span{display:block;color:var(--red)}
.back-head p{font-size:15px;line-height:18px;margin-top:12px;color:#333}
.services-title{left:34px;top:486px;color:var(--white);font-weight:700;font-size:22px;line-height:24px}
.service{width:240px;height:70px}
.service svg{position:absolute;left:0;top:0;width:66px;height:66px}
.service span{position:absolute;left:76px;top:4px;width:170px;color:var(--white);font-weight:500;font-size:16px;line-height:19px}
.why-title{left:38px;top:740px;color:var(--red);font-weight:800;font-size:25px;letter-spacing:3px}
.why-list{left:38px;top:780px;width:300px;list-style:none}
.why-list li{color:var(--white);font-weight:500;font-size:15px;height:31px;line-height:30px;border-bottom:1px dotted rgba(255,255,255,.35);display:flex;align-items:center;gap:8px}
.why-list li:last-child{border-bottom:none}
.tick{width:15px;height:15px;flex:none}
.worker{left:305px;top:720px;width:215px;height:320px;background:
 radial-gradient(ellipse at 60% 40%,#3e5f9e 0%,rgba(40,60,100,.5) 40%,rgba(0,0,0,0) 70%),
 linear-gradient(180deg,rgba(22,33,59,0) 0%,#3a2a1c 60%,#5a3c20 100%)}
.book{left:36px;top:922px;width:160px;color:var(--white);font-size:14px;line-height:17px}
.discount{left:180px;top:908px;text-align:center}
.discount b{display:block;font-weight:800;font-size:56px;line-height:54px;color:var(--yellow)}
.discount span{display:block;font-weight:800;font-size:18px;color:var(--white);line-height:18px}
.offer-note{left:36px;top:988px;width:268px;border:1.5px solid var(--white);background:var(--red);border-radius:4px;color:var(--white);font-size:9.5px;line-height:12px;font-weight:600;text-align:center;padding:3px 4px}
</style>
</head>
<body>

<!-- FRONT -->
<section class="hanger hanger--front" aria-label="Door hanger front">
  <div class="front-photo" role="img" aria-label="Photo: electrician in a hard hat working on a wired panel, power pylons against a dusk sky"></div>

  <svg class="layer" viewBox="0 0 520 1200" aria-hidden="true">
    <polygon points="0,935 520,665 520,1200 0,1200" fill="#fff"/>
    <polygon points="0,918 300,770 270,830 520,680 520,700 250,860 280,800 0,945" fill="#e8141b"/>
    <line x1="100" y1="0" x2="225" y2="100" stroke="#9a9a9a" stroke-width="4"/>
  </svg>

  <div class="hole"></div>

  <div class="abs brand">
    <div class="brand-name">K&amp;T</div>
    <div class="brand-sub">ELECTRIC, LLC</div>
  </div>

  <div class="abs front-head">
    <h1>Need a Reliable <span>Electrician?</span></h1>
    <p>Your Local Electrical Expert is Just Around the Corner!</p>
  </div>

  <svg class="abs offer-badge" viewBox="0 0 140 140" aria-hidden="true">
    <circle cx="70" cy="70" r="66" fill="#e8141b" stroke="#fff" stroke-width="3" stroke-dasharray="8 3"/>
  </svg>
  <div class="abs offer-text"><small>Special Offer</small><b>10%<br>OFF</b></div>
  <div class="abs offer-line">On Your<br>First<br>Service Call!</div>

  <div class="abs feature" style="left:20px">
    <svg viewBox="0 0 74 74"><polygon points="37,3 66,20 66,54 37,71 8,54 8,20" fill="#e8141b" stroke="#ffd400" stroke-width="4"/><circle cx="37" cy="39" r="14" fill="none" stroke="#fff" stroke-width="3"/><path d="M37 31v9l6 4" stroke="#fff" stroke-width="3" fill="none"/></svg>
    <span>Quick<br>Response<br>Times</span>
  </div>
  <div class="abs feature" style="left:138px">
    <svg viewBox="0 0 74 74"><polygon points="37,3 66,20 66,54 37,71 8,54 8,20" fill="#e8141b" stroke="#ffd400" stroke-width="4"/><circle cx="37" cy="32" r="11" fill="none" stroke="#fff" stroke-width="3"/><path d="M20 44c6 10 28 10 34 0" stroke="#fff" stroke-width="3" fill="none"/></svg>
    <span>Affordable<br>Rates</span>
  </div>
  <div class="abs feature" style="left:258px">
    <svg viewBox="0 0 74 74"><polygon points="37,3 66,20 66,54 37,71 8,54 8,20" fill="#e8141b" stroke="#ffd400" stroke-width="4"/><circle cx="37" cy="35" r="15" fill="none" stroke="#fff" stroke-width="3"/><path d="M30 35l5 5 9-10" stroke="#fff" stroke-width="3" fill="none"/></svg>
    <span>Quality<br>Workmanship</span>
  </div>
  <div class="abs feature" style="left:376px">
    <svg viewBox="0 0 74 74"><polygon points="37,3 66,20 66,54 37,71 8,54 8,20" fill="#e8141b" stroke="#ffd400" stroke-width="4"/><rect x="28" y="22" width="20" height="28" fill="none" stroke="#fff" stroke-width="3"/><path d="M32 30h12M32 36h12M32 42h8" stroke="#fff" stroke-width="2.5"/></svg>
    <span>Fully<br>Licensed &amp;<br>Insured</span>
  </div>

  <div class="abs tear"></div>
  <div class="abs call">
    <div class="call-label">CALL US TODAY</div>
    <div class="call-icon"><svg viewBox="0 0 24 24"><path d="M7 4l3 4-2 2c1 2 3 4 5 5l2-2 4 3-2 3C10 18 5 13 4 6z" fill="#1b1b1b"/></svg></div>
    <div class="call-num">(555) 318-4702</div>
  </div>
  <div class="abs link-box link-box--mail"><i class="link-dot"></i>info@kandtelectric.example</div>
  <div class="abs link-box link-box--web"><i class="link-dot"></i>www.kandtelectric.example</div>
  <p class="abs social"><i></i><b>Chatterpage</b><i></i><b>Pixmosaic</b><i></i><b>Quibbler</b><i></i><b>Linkloop</b> &nbsp;Follow Us on Social Media for More Tips and Special Offers!</p>
</section>

<!-- BACK -->
<section class="hanger hanger--back" aria-label="Door hanger back">
  <div class="abs back-photo" role="img" aria-label="Photo: power pylons at night" style="background:linear-gradient(160deg,#0c1425 0%,#1d2b4a 100%);clip-path:polygon(0 0,78% 0,0 94%)"></div>

  <svg class="layer" viewBox="0 0 520 1200" aria-hidden="true">
    <polygon points="0,238 300,95 330,100 0,262" fill="#e8141b"/>
    <polygon points="250,70 520,0 520,12 290,95" fill="#e8141b"/>
    <line x1="415" y1="0" x2="300" y2="100" stroke="#9a9a9a" stroke-width="4"/>
    <polygon points="0,410 300,490 318,440 520,545 520,1040 0,1040" fill="#15213b"/>
    <polygon points="0,393 300,473 325,418 520,528 520,548 318,452 300,505 0,418" fill="#e8141b"/>
  </svg>

  <div class="hole"></div>

  <svg class="abs emergency" viewBox="0 0 150 150" aria-hidden="true">
    <polygon points="75,4 138,40 138,110 75,146 12,110 12,40" fill="#fff" stroke="#1b1b1b" stroke-width="3" transform="rotate(-10 75 75)"/>
    <circle cx="110" cy="28" r="16" fill="#fff" stroke="#e8141b" stroke-width="3"/>
    <path d="M110 20v9l6 3" stroke="#e8141b" stroke-width="2.5" fill="none"/>
  </svg>
  <div class="abs emergency-text"><b>24<small>HR</small></b><span>EMERGENCY</span><em>SERVICE</em></div>

  <div class="abs back-head">
    <h2>Don't Let Electrical Issues <span>Keep You in the Dark!</span></h2>
    <p>From flickering lights to complete system upgrades,<br>we've got all your residential electrical needs covered.</p>
  </div>

  <div class="abs worker" role="img" aria-label="Photo: smiling electrician in hard hat and overalls giving thumbs up, holding a coil of cable"></div>

  <div class="abs services-title">OUR SERVICES<br>INCLUDE:</div>

  <div class="abs service" style="left:34px;top:552px">
    <svg viewBox="0 0 74 74"><polygon points="37,3 66,20 66,54 37,71 8,54 8,20" fill="#e8141b" stroke="#ffd400" stroke-width="4"/><path d="M40 20l-10 18h8l-4 16 12-20h-8z" fill="#fff"/></svg>
    <span>Electrical<br>Repairs &amp;<br>Troubleshooting</span>
  </div>
  <div class="abs service" style="left:290px;top:552px">
    <svg viewBox="0 0 74 74"><polygon points="37,3 66,20 66,54 37,71 8,54 8,20" fill="#e8141b" stroke="#ffd400" stroke-width="4"/><circle cx="37" cy="32" r="11" fill="none" stroke="#fff" stroke-width="3"/><path d="M32 46h10M33 51h8" stroke="#fff" stroke-width="3"/></svg>
    <span>Lighting<br>Installation<br>&amp; Upgrades</span>
  </div>
  <div class="abs service" style="left:34px;top:656px">
    <svg viewBox="0 0 74 74"><polygon points="37,3 66,20 66,54 37,71 8,54 8,20" fill="#e8141b" stroke="#ffd400" stroke-width="4"/><path d="M37 20l13 5v10c0 9-6 14-13 17-7-3-13-8-13-17V25z" fill="none" stroke="#fff" stroke-width="3"/><path d="M31 36l5 5 8-9" stroke="#fff" stroke-width="3" fill="none"/></svg>
    <span>Safety<br>Inspections &amp; Code<br>Compliance</span>
  </div>
  <div class="abs service" style="left:290px;top:656px">
    <svg viewBox="0 0 74 74"><polygon points="37,3 66,20 66,54 37,71 8,54 8,20" fill="#e8141b" stroke="#ffd400" stroke-width="4"/><path d="M26 48c0-14 10-24 24-24 0 14-10 24-24 24z" fill="none" stroke="#fff" stroke-width="3"/><path d="M26 48l14-14" stroke="#fff" stroke-width="3"/></svg>
    <span style="top:12px">Energy-Efficient<br>Solutions</span>
  </div>

  <div class="abs why-title">WHY CHOOSE US?</div>
  <ul class="abs why-list">
    <li><svg class="tick" viewBox="0 0 16 16"><circle cx="8" cy="8" r="7" fill="#fff" stroke="#e8141b" stroke-width="2"/><path d="M5 8l2 2 4-4" stroke="#e8141b" stroke-width="2" fill="none"/></svg>Friendly, Local Service</li>
    <li><svg class="tick" viewBox="0 0 16 16"><circle cx="8" cy="8" r="7" fill="#fff" stroke="#e8141b" stroke-width="2"/><path d="M5 8l2 2 4-4" stroke="#e8141b" stroke-width="2" fill="none"/></svg>Over 30 Years of Experience</li>
    <li><svg class="tick" viewBox="0 0 16 16"><circle cx="8" cy="8" r="7" fill="#fff" stroke="#e8141b" stroke-width="2"/><path d="M5 8l2 2 4-4" stroke="#e8141b" stroke-width="2" fill="none"/></svg>Satisfaction Guaranteed</li>
    <li><svg class="tick" viewBox="0 0 16 16"><circle cx="8" cy="8" r="7" fill="#fff" stroke="#e8141b" stroke-width="2"/><path d="M5 8l2 2 4-4" stroke="#e8141b" stroke-width="2" fill="none"/></svg>Upfront Pricing</li>
  </ul>

  <p class="abs book">Book Your<br>Appointment Now<br>and Claim Your</p>
  <div class="abs discount"><b>10%</b><span>DISCOUNT!</span></div>
  <p class="abs offer-note">Offer valid for new customers on the first visit only.<br>Mention this door hanger when booking.</p>

  <div class="abs tear"></div>
  <div class="abs call">
    <div class="call-label">CALL US TODAY</div>
    <div class="call-icon"><svg viewBox="0 0 24 24"><path d="M7 4l3 4-2 2c1 2 3 4 5 5l2-2 4 3-2 3C10 18 5 13 4 6z" fill="#1b1b1b"/></svg></div>
    <div class="call-num">(555) 318-4702</div>
  </div>
  <div class="abs link-box link-box--mail"><i class="link-dot"></i>info@kandtelectric.example</div>
  <div class="abs link-box link-box--web"><i class="link-dot"></i>www.kandtelectric.example</div>
  <p class="abs social"><i></i><b>Chatterpage</b><i></i><b>Pixmosaic</b><i></i><b>Quibbler</b><i></i><b>Linkloop</b> &nbsp;Follow Us on Social Media for More Tips and Special Offers!</p>
</section>

</body>
</html>
```